White Paper and One-Page Advertisement for TELVAMORE-QX

I need both documents to be better formatted and designed so they look professional, not something someone with mediocre word skills put together. They will go out to 1000s of industry professionals, and they need to look sharp. I need them to have my company's color palate logo, and branding on it similar to how it is now, but better. Please do not change any of the written content, but it can be arranged in any other format you think is better. Smart art and things i've already used can be omitted in favor of better designs. The developer is free to use their creativity. White paper should not be longer than the three pages unless necessary.

Target Market(s)

Life Sciences supply chain professionals

Colors
33b8a4
0592cd
9bcb3c
fbee3e
3277b5

Requirements
Must have
• Must be professional looking and not look like something done in word. Please use the color palate as seen on the documents.
Should not have
• Any changes to the written content.

```html
<!DOCTYPE html>
<html lang="en">
<head>
<meta charset="utf-8">
<title>TELVAMORE-QX One-Page Advertisement</title>
<link rel="stylesheet" href="https://fonts.googleapis.com/css2?family=Montserrat:wght@400;500;700;800&display=swap">
<style>
:root{
  --teal:#1b7f71;
  --green:#9bcb3c;
  --mint:#86cc9e;
  --aqua:#5bc6cf;
  --sea:#4da7ad;
  --cyan:#1ab0d8;
  --lime-num:#c8e04a;
  --ink:#2e2e2e;
  --orange:#f08a24;
  --page-bg:#e6e8e8;
}
*{margin:0;padding:0;box-sizing:border-box}
html,body{width:1200px;height:1200px;overflow:hidden;background:var(--page-bg);font-family:"Montserrat",sans-serif}
.flyer{position:absolute;left:150px;top:18px;width:978px;height:1265px;background:#fff;transform:scale(.92);transform-origin:top left;color:var(--ink)}
.abs{position:absolute}
.brand{left:735px;top:40px;width:200px;text-align:center}
.brand-dot{width:44px;height:44px;border-radius:50%;background:var(--teal);margin:0 auto 12px}
.brand-name{font-weight:800;font-size:22px;color:var(--teal);letter-spacing:.5px}
.section-tab{left:48px;top:107px;height:45px;width:202px;background:var(--teal);color:#fff;font-weight:700;font-size:25px;line-height:45px;padding-left:17px;border-radius:0 3px 3px 0}
.timeline{left:48px;top:152px;width:2px;height:352px;background:var(--teal)}
.dot{width:13px;height:13px;border-radius:50%;background:var(--teal);left:42px}
.point{left:66px;width:840px;font-size:18.5px;line-height:20px;font-weight:500;color:#333}
.process{left:93px;top:309px}
.benefits{left:0;top:560px;width:978px;height:167px;background:linear-gradient(90deg,#8cc63f 0%,#6ac48a 45%,#3cbdb0 75%,#1ab0d8 100%)}
.benefits h2{position:absolute;left:64px;top:6px;color:#fff;font-size:25px;font-weight:700}
.benefit{position:absolute;top:40px}
.benefit .num{position:absolute;left:0;top:0;font-size:38px;font-weight:500;color:var(--lime-num);line-height:38px}
.benefit .rule{position:absolute;left:11px;top:38px;width:1.5px;background:var(--lime-num)}
.benefit p{position:absolute;top:4px;color:#fff;font-size:15.5px;line-height:20.5px;font-weight:500}
.promise-label{left:48px;top:782px;width:202px;height:64px;background:var(--green);color:#fff;font-weight:800;font-size:27px;line-height:64px;text-align:center;box-shadow:0 4px 6px rgba(0,0,0,.2)}
.promise-text{left:254px;top:782px;width:631px;height:64px;background:var(--teal);color:#fff;font-weight:700;font-size:18.5px;line-height:21px;padding:9px 0 0 38px;box-shadow:0 4px 6px rgba(0,0,0,.2)}
.photo{left:105px;top:905px;width:337px;height:224px;background:linear-gradient(135deg,#6b4a2e,#a8753f 45%,#e3ddd2 60%,#3e5a55)}
.about-rule{left:499px;top:960px;width:2px;height:104px;background:var(--orange)}
.about{left:515px;top:960px;width:375px;font-size:15px;line-height:17px;text-align:justify;color:#222}
.about b{font-weight:700}
.about p+p{margin-top:18px}
.footer{left:0;top:1177px;width:978px;height:88px;background:var(--teal);color:#fff;font-size:19px;line-height:88px;text-align:center}
.footer b{font-weight:700}
.footer .sep{margin:0 12px}
</style>
</head>
<body>
<div class="flyer">
  <div class="abs brand"><div class="brand-dot"></div><div class="brand-name">TELVAMORE-QX</div></div>

  <div class="abs section-tab">Our Platform</div>
  <div class="abs timeline"></div>
  <div class="abs dot" style="top:184px"></div>
  <div class="abs dot" style="top:245px"></div>
  <div class="abs dot" style="top:414px"></div>
  <div class="abs dot" style="top:455px"></div>
  <div class="abs dot" style="top:496px"></div>

  <div class="abs point" style="top:181px">A multi-vendor marketplace for the life science community to transact pre-market and after-market materials and equipment</div>
  <div class="abs point" style="top:243px">Researchers, manufactures, and original suppliers can create an account to buy, sell, or donate materials</div>

  <svg class="abs process" width="792" height="67" viewBox="0 0 792 67" aria-label="Platform process">
    <path d="M632 0H785a7 7 0 0 1 7 7V60a7 7 0 0 1-7 7H632l18-33.5z" fill="var(--sea)"/>
    <path d="M370 0H632l18 33.5L632 67H370l18-33.5z" fill="var(--aqua)"/>
    <path d="M203 0H370l18 33.5L370 67H203l18-33.5z" fill="var(--mint)"/>
    <path d="M7 0H203l18 33.5L203 67H7a7 7 0 0 1-7-7V7a7 7 0 0 1 7-7z" fill="var(--green)"/>
    <g fill="#fff" font-family="Montserrat, sans-serif" font-weight="700">
      <text x="32" y="29" font-size="17">Authentication &amp;</text>
      <text x="32" y="49" font-size="17">terms of quality</text>
      <text x="242" y="39" font-size="17">Set up store</text>
      <text x="409" y="29" font-size="17">Seamlessly trasnact &amp;</text>
      <text x="409" y="49" font-size="17">request for information</text>
      <text x="681" y="30" font-size="15">Check out</text>
      <text x="681" y="47" font-size="15">and sign</text>
    </g>
  </svg>

  <div class="abs point" style="top:411px">Part 11 compliant signature and authentication</div>
  <div class="abs point" style="top:452px">Leverages industry auditing skills to facilitate compliant and transparent transactions</div>
  <div class="abs point" style="top:493px">Some of the best and industry vendors and software used</div>

  <section class="abs benefits">
    <h2>Benefits</h2>
    <div class="benefit" style="left:36px"><span class="num">1</span><span class="rule" style="height:82px"></span><p style="left:28px;width:160px">Reduce write-offs by selling excess &amp; obsolete materials, equipment, spare parts, etc.</p></div>
    <div class="benefit" style="left:212px"><span class="num">2</span><span class="rule" style="height:62px"></span><p style="left:35px;width:100px">Buy quality materials at a reduced price.</p></div>
    <div class="benefit" style="left:343px"><span class="num">3</span><span class="rule" style="height:62px"></span><p style="left:32px;width:95px">Market materials if an original supplier</p></div>
    <div class="benefit" style="left:469px"><span class="num">4</span><span class="rule" style="height:62px"></span><p style="left:26px;width:100px">Donate material to researchers</p></div>
    <div class="benefit" style="left:598px"><span class="num">5</span><span class="rule" style="height:40px"></span><p style="left:23px;width:90px">Acquire donated materials</p></div>
    <div class="benefit" style="left:700px"><span class="num">6</span><span class="rule" style="height:82px"></span><p style="left:23px;width:200px">Collaborate and consort to reduce supply chain risk such as mutual aid agreements, joint supplier audits, etc.</p></div>
  </section>

  <div class="abs promise-label">Our Promise</div>
  <div class="abs promise-text">A greener, more cost-efficient, and quality driven supply chain through a collaborativelife sciences marketplace.</div>

  <div class="abs photo" role="img" aria-label="Photograph of people sharing a warm moment together at a traditional ceremony"></div>
  <div class="abs about-rule"></div>
  <div class="abs about">
    <p><b>TELVAMORE-QX</b> aspires to change the waste and risk paradigm in the life science industry.</p>
    <p>We strive to make companies better stewards of their dollars and our environment to transfer benefit to them...THE PATIENT</p>
  </div>

  <footer class="abs footer"><b>Web</b> www.telvamoreqx.com<span class="sep">|</span><b>Email</b> info@telvamoreqx.com<span class="sep">|</span><b>Read our</b> white paper</footer>
</div>
</body>
</html>
```